Double-sided half page marketing handout for professional association conference

We need a collatoral piece that will go into conference attendees' registration packets. Handout will be double-sided, half-letter-sized page. Working print area is 8.1" by 5.3" for each side. Can be laid out either vertically or horizontally.

One side of the piece will be focused on my firm's contact information and broad scope of services:

Contact Information:
Halvick Partners LLC
Local Government Consultants
555-314-0297
www.halvickpartners.example
info@halvickpartners.example

Services:
Bond Rating Assessments
Economic Development Consulting
Executive Dashboards
Public Policy Analysis
Governance Training & Support
Strategic Planning & Performance Management

The other side of the piece will focus on the Bond Rating Assessments (see http://www.halvickpartners.example/Pages/Bond-Rating-Assessments.aspx and attachments for more detail). This side should contain the text:

"Considering issuing debt? Bond ratings make a difference. Did you know that on an average $20 million GO debt issuance a one rating-level difference can easily equate to over $350,000 in interest cost-savings under normal market conditions?

The ratings agencies use a combined quantitative and qualitative approach to arrive at your bond rating. Our Bond Ratings Assessment shows you precisely what the agencies are looking at, provides advice as to how to frame the conversation during ratings calls, and identifies both strategic opportunities to provide upgrade pressure and specific threats that may lead to a downgrade. Call or email us to find out more or to get an example assessment."

Go to www.halvickpartners.example and see attached files for logo and a recent winning ArtBazaarly 1/4 page advertisement for style guidance.

Target Market(s)

Highly-educated, conservative local government executives.

Industry/Entity Type

Marketing

Font styles to use
Sans Serif

Colors
3277b5
85acd3
ffffff

Requirements
Must have
• Our logo, our contact information, basic information stated in Project Description. Feel free to modify language to make more clear or understandable.
Nice to have
• We rather not just a text piece - bringing in some graphical elements would be very nice.

```html
<!DOCTYPE html>
<html lang="en">
<head>
<meta charset="utf-8">
<title>Halvick Partners LLC — Conference Handout</title>
<link rel="stylesheet" href="https://fonts.googleapis.com/css2?family=Open+Sans:wdth,wght@75..100,300..800&display=swap">
<style>
  :root {
    --brand-blue: #3277b5;
    --brand-blue-light: #5fb6e6;
    --brand-blue-soft: #85acd3;
    --white: #ffffff;
    --ink: #111111;
    --ink-gray: #555555;
    --stage: #6b6b6b;
    --logo-gray: #8a8a8a;
  }
  * { margin: 0; padding: 0; box-sizing: border-box; }
  html, body { width: 1200px; height: 900px; overflow: hidden; }
  body {
    background: var(--stage);
    font-family: "Open Sans", Arial, sans-serif;
    position: relative;
  }
  .side {
    position: absolute;
    top: 58px;
    width: 487px;
    height: 772px;
    overflow: hidden;
    box-shadow: 0 2px 10px rgba(0,0,0,.45);
  }

  /* ---------- Front: bond ratings ---------- */
  .side--front {
    left: 81px;
    background: var(--white);
  }
  .front-hero {
    position: absolute; left: 0; top: 0; width: 100%; height: 420px;
    background: radial-gradient(ellipse 70% 60% at 65% 70%, var(--brand-blue-light) 0%, var(--brand-blue) 75%);
  }
  .front-logo {
    position: absolute; left: 0; top: 25px; width: 172px; height: 94px;
    background: var(--white);
    display: flex; align-items: center; justify-content: center;
    text-align: center;
    font-size: 18px; font-weight: 600; line-height: 1.15; color: var(--ink);
    box-shadow: 0 2px 6px rgba(0,0,0,.3);
  }
  .front-headline {
    position: absolute; left: 27px; top: 140px;
    color: var(--white);
    line-height: 1;
  }
  .front-headline .line-light { display: block; font-size: 58px; font-weight: 400; letter-spacing: .5px; }
  .front-headline .line-bold { display: block; font-size: 40.5px; font-weight: 700; margin-top: 8px; }
  .front-visual {
    position: absolute; left: 62px; top: 264px; width: 160px; height: 210px;
    border-radius: 6px;
    background: linear-gradient(135deg, #e8e8e8 0%, #a9a9a9 55%, #d9b44a 100%);
  }
  .front-stat {
    position: absolute; left: 27px; top: 498px; width: 250px;
    font-size: 16.5px; font-weight: 700; text-transform: uppercase;
    color: var(--brand-blue); line-height: 23px;
  }
  .front-stat strong { color: var(--ink); font-size: 21px; font-weight: 700; }
  .front-divider {
    position: absolute; left: 296px; top: 452px; width: 1px; height: 260px;
    background: linear-gradient(to bottom, transparent, #bbb 20%, #bbb 80%, transparent);
  }
  .front-detail {
    position: absolute; left: 321px; top: 442px; width: 145px;
  }
  .front-detail h2 {
    font-size: 12.5px; font-weight: 700; color: var(--ink); line-height: 14px; margin-bottom: 18px;
  }
  .front-detail p {
    font-size: 11px; color: var(--ink-gray); line-height: 13.5px;
  }
  .front-detail p b { color: #333; font-weight: 700; }
  .front-cta {
    position: absolute; left: 0; bottom: 0; width: 100%; height: 46px;
    background: var(--brand-blue);
    color: var(--white); font-size: 11.5px; font-weight: 700; text-transform: uppercase;
    display: flex; align-items: center; justify-content: center;
  }

  /* ---------- Back: contact & services ---------- */
  .side--back {
    left: 619px;
    background: linear-gradient(to bottom, #3d86c4 0%, var(--brand-blue) 100%);
    font-stretch: 80%;
  }
  .back-contact {
    position: absolute; left: 0; top: 0; width: 100%; height: 137px;
    background: linear-gradient(to bottom, var(--brand-blue) 0%, var(--brand-blue-light) 100%);
    color: var(--white); text-align: center;
  }
  .back-contact .tagline { position: absolute; top: 20px; width: 100%; font-size: 25px; font-weight: 400; }
  .back-contact .phone { position: absolute; top: 50px; width: 100%; font-size: 33px; font-weight: 700; color: var(--ink); font-stretch: 85%; }
  .back-contact .links {
    position: absolute; top: 96px; width: 100%; font-size: 20px; font-weight: 600;
    display: flex; justify-content: center; gap: 22px;
  }
  .back-logo {
    position: absolute; left: 0; top: 137px; width: 100%; height: 178px;
    background: var(--white);
    display: flex; align-items: center; justify-content: center;
    font-size: 44px; font-weight: 500; color: var(--logo-gray); font-stretch: 100%;
    box-shadow: 0 3px 8px rgba(0,0,0,.3);
  }
  .back-heading {
    position: absolute; top: 364px; width: 100%; text-align: center;
    font-size: 37px; font-weight: 300; color: var(--ink); letter-spacing: .5px;
  }
  .services {
    position: absolute; top: 432px; width: 100%; list-style: none; text-align: center;
    color: var(--white); font-size: 27px; font-weight: 400; text-transform: uppercase; line-height: 40px;
  }
  .services li.wrap { line-height: 32px; margin-top: 4px; }
</style>
</head>
<body>

<section class="side side--front" aria-label="Bond rating assessments side">
  <div class="front-hero"></div>
  <div class="front-logo">Halvick Partners<br>LLC</div>
  <h1 class="front-headline">
    <span class="line-light">BOND RATINGS</span>
    <span class="line-bold">MAKE A DIFFERENCE</span>
  </h1>
  <div class="front-visual" role="img" aria-label="Open steel vault holding stacked gold bars"></div>

  <p class="front-stat">Did you know that on an average <strong>$20 million</strong> G.O. debt issuance a single rating-level upgrade easily equates to about <strong>$350,000</strong> in interest savings under normal market conditions?</p>

  <div class="front-divider"></div>

  <div class="front-detail">
    <h2>Go beyond the fund balance, which only makes up between 10% and 20% of your final rating.</h2>
    <p>Our Bond Ratings Assess­ment shows you <b>precisely</b> what the agencies are look­ing at, provides advice as to how to <b>frame the conver­sation</b> during ratings calls, and identifies both <b>strategic opportunities</b> to provide upgrade pressure and specific threats that may lead to a downgrade.</p>
  </div>

  <div class="front-cta">Call or email us to find out more or to get an example assessment.</div>
</section>

<section class="side side--back" aria-label="Contact and services side">
  <div class="back-contact">
    <div class="tagline">Local Government Consultants</div>
    <div class="phone">555-314-0297</div>
    <div class="links"><span>www.halvickpartners.example</span><span>info@halvickpartners.example</span></div>
  </div>
  <div class="back-logo">Halvick Partners LLC</div>
  <h2 class="back-heading">SOLUTIONS | DELIVERED</h2>
  <ul class="services">
    <li>Bond Rating Assessments</li>
    <li>Economic Development Consulting</li>
    <li>Executive Dashboards</li>
    <li>Public Policy Analysis</li>
    <li>Governance Training &amp; Support</li>
    <li class="wrap">Strategic Planning &amp; Performance<br>Management</li>
  </ul>
</section>

</body>
</html>
```